Business Card Design Project

I want a cleaner business card and envelope then what we have now, its too crowded.
Updates

I update with logo, this can be changed anyway you feel it looks best. I also have put gaurantee on there and extended time, this is my first time doing this. Also gave an example of current card

Target Market(s)

a wide array of customers from lattice 700 to small companies and cleints

Industry/Entity Type

Business

Requirements
Must have
• Need to have address, telephone number email
Nice to have
• a sharp professional card that stands out but is still very clean.
Should not have
• Not crazy looking

```html
<!DOCTYPE html>
<html lang="en">
<head>
<meta charset="utf-8">
<title>Halden Insurance Group – Business Cards</title>
<link rel="stylesheet" href="https://fonts.googleapis.com/css2?family=Open+Sans:wght@400;600;700&display=swap">
<style>
  :root {
    --page-bg: #e9e9e7;
    --card-dark: #3b3b3d;
    --card-dark-deep: #2a2a2c;
    --silver-light: #fbfbfb;
    --silver-mid: #d6d6d8;
    --silver-deep: #a9a9ad;
    --text-light: #f2f2f2;
    --text-dark: #3a3a3c;
  }
  html, body {
    margin: 0;
    width: 1200px;
    height: 1023px;
    overflow: hidden;
    background: var(--page-bg);
    font-family: "Open Sans", Arial, sans-serif;
  }
  .sheet {
    position: relative;
    width: 1200px;
    height: 1023px;
  }
  .card {
    position: absolute;
    left: 250px;
    width: 700px;
    height: 400px;
    box-shadow: 0 10px 28px rgba(0,0,0,0.22);
  }
  .card--back { top: 80px; }
  .card--front { top: 543px; }
  .card svg { display: block; }
  .heading { font-weight: 700; font-size: 13px; fill: var(--text-light); letter-spacing: 0.4px; }
  .item { font-size: 12.5px; fill: var(--text-light); }
  .holder-name { font-weight: 700; font-size: 21px; fill: var(--text-light); }
  .holder-title { font-size: 13px; fill: var(--text-light); }
  .contact { font-size: 13px; fill: var(--text-light); }
  .brand-name { font-weight: 600; fill: var(--text-dark); }
  .brand-mark { fill: var(--text-dark); }
</style>
</head>
<body>
<main class="sheet">

  <!-- Back of card: list of services -->
  <section class="card card--back" aria-label="Business card back">
    <svg width="700" height="400" viewBox="0 0 700 400">
      <defs>
        <linearGradient id="silverBack" x1="0" y1="0" x2="1" y2="1">
          <stop offset="0" stop-color="var(--silver-light)"/>
          <stop offset="0.55" stop-color="var(--silver-mid)"/>
          <stop offset="1" stop-color="var(--silver-deep)"/>
        </linearGradient>
        <linearGradient id="darkBack" x1="0" y1="0" x2="0" y2="1">
          <stop offset="0" stop-color="var(--card-dark)"/>
          <stop offset="1" stop-color="var(--card-dark-deep)"/>
        </linearGradient>
      </defs>
      <rect class="card-base" width="700" height="400" fill="url(#silverBack)"/>
      <path class="wave-highlight" d="M0,215 C200,265 330,292 430,252 C520,216 600,192 700,188 V205 C600,210 520,238 430,275 C320,318 190,290 0,240 Z" fill="#ffffff" opacity="0.85"/>
      <path class="wave-dark" d="M0,0 H700 V175 C600,180 520,205 420,245 C330,280 200,255 0,205 Z" fill="url(#darkBack)"/>

      <g class="service-column" transform="translate(40,48)">
        <text class="heading" y="0">COMMERCIAL INSURANCE</text>
        <text class="item" y="22">• Traditional Insurance Coverage</text>
        <text class="item" y="42">• Executive Protection Coverage</text>
        <text class="item" y="62">• Specialty Coverage Insurance</text>
      </g>
      <g class="service-column" transform="translate(270,48)">
        <text class="heading" y="0">PERSONAL INSURANCE</text>
        <text class="item" y="22">• Auto/Recreational/Boat</text>
        <text class="item" y="42">• Home/Renters/Condo</text>
        <text class="item" y="62">• Umbrella Liability</text>
      </g>
      <g class="service-column" transform="translate(460,48)">
        <text class="heading" y="0">EMPLOYEE BENEFITS</text>
        <text class="item" y="22">• Medical/Dental/Optical Plans</text>
        <text class="item" y="42">• Prescription Coverage</text>
        <text class="item" y="62">• Life &amp; Accidental Death</text>
        <text class="item" y="82">  &amp; Dismemberment Insurance</text>
        <text class="item" y="102">• Disability Insurance</text>
        <text class="item" y="122">• Voluntary Benefits</text>
      </g>

      <g class="brand" transform="translate(400,335)">
        <text class="brand-name" font-size="30" letter-spacing="5">HALDEN</text>
        <text class="brand-name" y="24" font-size="14" letter-spacing="3.2">INSURANCE GROUP</text>
      </g>
    </svg>
  </section>

  <!-- Front of card: contact details -->
  <section class="card card--front" aria-label="Business card front">
    <svg width="700" height="400" viewBox="0 0 700 400">
      <defs>
        <linearGradient id="silverFront" x1="0" y1="0" x2="1" y2="1">
          <stop offset="0" stop-color="var(--silver-deep)"/>
          <stop offset="0.45" stop-color="var(--silver-light)"/>
          <stop offset="1" stop-color="var(--silver-mid)"/>
        </linearGradient>
        <linearGradient id="darkFront" x1="0" y1="0" x2="1" y2="1">
          <stop offset="0" stop-color="var(--card-dark)"/>
          <stop offset="1" stop-color="var(--card-dark-deep)"/>
        </linearGradient>
      </defs>
      <rect class="card-base" width="700" height="400" fill="url(#silverFront)"/>
      <path class="wave-highlight" d="M0,200 C150,212 330,242 440,282 C530,315 545,400 640,400 H620 C545,400 520,318 432,288 C320,252 150,222 0,215 Z" fill="#ffffff" opacity="0.9"/>
      <path class="wave-dark" d="M0,0 H700 V400 H620 C540,400 520,300 440,270 C330,230 150,200 0,190 Z" fill="url(#darkFront)"/>

      <g class="holder" transform="translate(430,62)">
        <text class="holder-name" y="0">Marla Quenby-Roth</text>
        <text class="holder-title" y="22">Operations Manager</text>
        <text class="contact" y="62">18720 Orchard Ave,</text>
        <text class="contact" y="82">Brookfield Hills, MI 48200</text>
        <text class="contact" y="122">phone: 555-210-4700 ext. 118</text>
        <text class="contact" y="141">direct: 555-210-4791</text>
        <text class="contact" y="160">fax: 555-210-4705</text>
        <text class="contact" y="179">email: m.quenby-roth@haldeninsure.com</text>
        <text class="contact" y="198">web: www.haldeninsure.com</text>
      </g>

      <g class="brand" transform="translate(55,305)">
        <rect class="brand-mark" x="0" y="0" width="42" height="42"/>
        <text class="brand-name" x="56" y="24" font-size="30" letter-spacing="5">HALDEN</text>
        <text class="brand-name" x="56" y="44" font-size="14" letter-spacing="3.2">INSURANCE GROUP</text>
      </g>
    </svg>
  </section>

</main>
</body>
</html>
```